A 'new law' boutique Australian law firm that provides specialist employment law and people managem

We value helping clients create results with respect workplaces. What differentiates us is we provide actionable training in understanding and dealing with people and ensure legal compliance fits with this approach. We would like a fresh approach to our training overview documents that we currently use in our current law firm (6 attached). Please use pictures, symbols etc consistent with our non-traditional law approach that captures the approach of each training session.. Attached is the logo and draft letterhead for Brindle Legal which will launch soon.

Target Market(s)

HR Managers and in-house lawyers (non employment specialists) in mid-large Australian companies that are progressive with a relationship based approach to managing employee behaviours and disputes.

Industry/Entity Type

Human Resource

Font styles to use
Sans Serif

Colors
3176b5
33a6d7

Requirements
Must have
• 1 or 2 page PDF for each of the 6 documents that the wording supplied goes into your design which will be pretty similar as we want consistency with our documents

```html
<!DOCTYPE html>
<html lang="en">
<head>
<meta charset="utf-8">
<title>Brindle Legal – Training Overviews</title>
<link href="https://fonts.googleapis.com/css2?family=Open+Sans:wght@400;600;700&display=swap" rel="stylesheet">
<style>
:root{
  --blue:#3176b5;
  --sky:#33a6d7;
  --ink:#2b2b2b;
  --muted:#6b6f73;
  --panel:#eceeef;
  --panel-dark:#d9dcde;
  --footer-grey:#7d8489;
  --bg:#dfe4e4;
  --white:#ffffff;
}
*{box-sizing:border-box;margin:0;padding:0}
html,body{width:1200px;height:1200px;overflow:hidden}
body{background:var(--bg);font-family:"Open Sans",Arial,sans-serif;color:var(--ink);position:relative}
.flyer{position:absolute;top:218px;width:540px;height:764px;background:var(--white);box-shadow:0 6px 18px rgba(0,0,0,.18);overflow:hidden}
.flyer--conflict{left:45px}
.flyer--communication{left:615px}
.brand{position:absolute;top:34px;left:34px;display:flex;align-items:center;gap:8px;color:var(--blue);font-size:20px;font-weight:600;letter-spacing:.5px}
.brand__dot{width:14px;height:14px;border-radius:50%;background:var(--sky)}
.title{position:absolute;right:30px;color:var(--blue);font-weight:400;text-transform:uppercase;text-align:right;line-height:1.15}
.photo{position:absolute;left:0;width:100%}
.need-box{position:absolute;background:var(--blue);color:var(--white);padding:12px 14px}
.need-box h3,.section-head{font-size:10px;font-weight:600;text-transform:uppercase;letter-spacing:.3px}
.need-box p{font-size:7px;line-height:1.5;margin-top:6px}
.section-head{position:absolute;color:var(--blue);border-bottom:1px solid var(--blue);padding-bottom:2px}
.topics{position:absolute;display:grid;gap:0;background:var(--panel)}
.topic{display:grid;grid-template-columns:70px 1fr;border-bottom:1px solid var(--white)}
.topic__label{background:var(--panel-dark);color:var(--blue);font-size:7px;font-weight:700;padding:8px 6px}
.topic__body{font-size:6.5px;line-height:1.5;padding:8px 8px;color:var(--ink)}
.topic__body ul{padding-left:9px}
.outcomes{position:absolute;font-size:6.5px;line-height:1.55}
.outcomes ol{padding-left:10px}
.footer{position:absolute;left:0;bottom:0;width:100%;height:64px;display:flex}
.footer__contact{background:var(--blue);color:var(--white);width:54%;font-size:8px;padding:12px 30px;display:flex;flex-direction:column;justify-content:space-between;clip-path:polygon(0 0,100% 0,100% 100%,0 100%)}
.footer__social{background:var(--footer-grey);color:var(--white);flex:1;font-size:8px;padding:12px 24px;display:flex;flex-direction:column;justify-content:space-between}
.line-item{display:flex;align-items:center;gap:6px}
.line-item::before{content:"";width:7px;height:7px;border-radius:50%;background:var(--white);display:inline-block}
</style>
</head>
<body>

<article class="flyer flyer--conflict">
  <div class="brand"><span class="brand__dot"></span>Brindle Legal</div>
  <h1 class="title" style="top:62px;font-size:19px">Managing Conflict and<br>Complaints (Conduct)</h1>
  <div class="photo" style="top:118px;height:215px;background:linear-gradient(120deg,#6b3a1c 0%,#c79a2e 30%,#3a2414 60%,#141414 100%)" role="img" aria-label="Photograph of gold law books, scales of justice and a wooden gavel on a desk"></div>
  <section class="need-box" style="left:325px;top:140px;width:190px;height:222px">
    <h3>Training Need</h3>
    <p>Unlawful or inappropriate behaviour in the workplace that is left unaddressed can impact on productivity, staff retention and the reputation of your organisation. Clear policies and procedures help managers respond early. This training explains the options available to Contact Officers so they can guide staff with confidence and support a safe and respectful workplace.</p>
  </section>
  <h2 class="section-head" style="left:30px;top:345px">Overview of Training</h2>
  <div class="topics" style="left:30px;top:368px;width:245px">
    <div class="topic"><div class="topic__label">Discrimination</div><div class="topic__body">What is direct and indirect discrimination? What are the exceptions to the general rules? Practical examples of behaviour that may be discriminatory.</div></div>
    <div class="topic"><div class="topic__label">Harassment</div><div class="topic__body">What is harassment? Are protected attributes relevant to harassment? What is the difference between harassment and sexual harassment? Practical examples of behaviour that may be harassment.</div></div>
    <div class="topic"><div class="topic__label">Bullying</div><div class="topic__body">What is bullying? Explore how bullying differs to reasonable management action. Practical examples of behaviour that may be bullying.</div></div>
  </div>
  <div class="topics" style="left:280px;top:368px;width:235px">
    <div class="topic"><div class="topic__label">Victimisation and Vilification</div><div class="topic__body">What is victimisation? What is Vilification?</div></div>
    <div class="topic"><div class="topic__label">Adverse Action</div><div class="topic__body">What is adverse action and how does it differ to other unlawful behaviour? When is it lawful to terminate employment because of a protected attribute?</div></div>
    <div class="topic"><div class="topic__label">Grievance Options</div><div class="topic__body">Explore the options of complaint management, formal and informal. How do they compare and what are the advantages and disadvantages of each approach? Who decides which option?</div></div>
    <div class="topic"><div class="topic__label">Test Learning</div><div class="topic__body">Role play, group discussion</div></div>
  </div>
  <h2 class="section-head" style="left:30px;top:585px">Learning Outcomes</h2>
  <div class="outcomes" style="left:30px;top:606px;width:240px">
    <p>Training will enable participants to perform their role of Contact Officer and to understand:</p>
    <ol>
      <li>The role and responsibilities of a Contact Officer</li>
      <li>What amounts to unlawful workplace behaviour</li>
      <li>What is considered inappropriate behaviour in our workplace</li>
    </ol>
  </div>
  <div class="outcomes" style="left:285px;top:606px;width:230px">
    <ol start="4">
      <li>How to apply understanding unlawful/inappropriate behaviour to common scenarios</li>
      <li>How to address and resolve grievances early</li>
      <li>Options to resolve grievances internally and the Contact Officer role</li>
      <li>External options and their pros and cons for resolving grievances</li>
    </ol>
  </div>
  <footer class="footer">
    <div class="footer__contact"><span class="line-item">www.brindlelegal.com.au</span><span class="line-item">info@brindlelegal.com.au</span></div>
    <div class="footer__social"><span class="line-item">brindlelegal</span><span class="line-item">brindlelegal</span></div>
  </footer>
</article>

<article class="flyer flyer--communication">
  <div class="brand"><span class="brand__dot"></span>Brindle Legal</div>
  <h1 class="title" style="top:72px;font-size:19px">Effective Communication</h1>
  <div class="photo" style="top:110px;height:205px;background:linear-gradient(110deg,#1c1612 0%,#5a4630 40%,#b59a6c 70%,#3a2c20 100%)" role="img" aria-label="Photograph of brass scales of justice, an open book and a gavel in a library"></div>
  <section class="need-box" style="left:0;top:298px;width:540px;height:90px;padding:12px 30px">
    <h3>Training Need</h3>
    <p>Effective communication is critical for interacting with managers, work colleagues, clients and suppliers. Workplaces must continuously resolve conflict, which is natural because people don't see things the same way. Many complaints arise out of poor communication. DISC is a behavioural style tool that is easy to apply and highly effective. We are accredited DISC Trainers and apply this tool in all of our training.</p>
  </section>
  <h2 class="section-head" style="left:30px;top:400px">Overview of Training</h2>
  <div class="topics" style="left:30px;top:422px;width:245px">
    <div class="topic"><div class="topic__label">Understanding what is and isn't effective communication</div><div class="topic__body"><ul><li>Introduction to DISC</li><li>Explanation of DISC styles</li><li>Interpreting DISC styles from verbal, vocal and visual behaviours</li></ul></div></div>
    <div class="topic"><div class="topic__label">Applying DISC to the Workplace</div><div class="topic__body"><ul><li>Understanding how each DISC style impacts on communication in the workplace</li><li>Tips and Traps of the DISC styles and how they can create/resolve workplace conflict</li></ul></div></div>
  </div>
  <div class="topics" style="left:280px;top:422px;width:235px">
    <div class="topic"><div class="topic__label">Advanced DISC style interpretation</div><div class="topic__body"><ul><li>Understanding dominant and secondary DISC styles and determining subtleties and variations in a workplace context</li></ul></div></div>
    <div class="topic"><div class="topic__label">Activities</div><div class="topic__body"><ul><li>Identifying strengths and weaknesses with team members</li><li>Performance improvement</li><li>Team profiles and dynamics</li><li>Effective emails and communication with colleagues</li><li>Resolving conflict scenarios</li></ul></div></div>
  </div>
  <h2 class="section-head" style="left:30px;top:590px">Learning Outcomes</h2>
  <div class="outcomes" style="left:30px;top:611px;width:230px">
    <p>Participants will practise and apply the learnings to:</p>
    <ol>
      <li>use DISC to understand their management style and the how to adjust their style to build relationships</li>
    </ol>
  </div>
  <div class="outcomes" style="left:280px;top:611px;width:235px">
    <ol start="2">
      <li>be more effective in a range of workplace situations including being more genuinely open to: (a) performance conversations; (b) resolving conflicts and complaints and understanding team dynamics; and (c) identifying strengths based gaps; and</li>
      <li>roll out similar training so managers can roll out DISC and apply it to their teams.</li>
    </ol>
  </div>
  <footer class="footer">
    <div class="footer__contact"><span class="line-item">www.brindlelegal.com.au</span><span class="line-item">info@brindlelegal.com.au</span></div>
    <div class="footer__social"><span class="line-item">brindlelegal</span><span class="line-item">brindlelegal</span></div>
  </footer>
</article>

</body>
</html>
```